International Business Consulting Company Website

RK Harbor Advisors is a U.S-based international consulting firm. We combined passion for success in the global business arena with hands-on experience to help foreign companies navigate the entry into U.S. markets and U.S. companies in initiating and expanding exports to foreign markets.

We need a simple 1 page website
Examples of other consultants’ websites:
http://www.brindlemarkgroup.example/#intro
https://www.tpq-advisory.example
http://morivetagroup.example
https://quillstoneadvisors.example

I also need the designer to suggest stock images that are suitable (related to international business, exports).

We want our web design to be bold, yet clean and simple.

Target Market(s)

US companies that export abroad, foreign companies that want to do business int he US/ open a subsidiary in the US.

Industry/Entity Type

Business Consultant

Coding

Coded - Design and coding required

Font styles to use
Sans Serif

Requirements
Must have
• Company logo on top

```html
<!DOCTYPE html>
<html lang="en">
<head>
<meta charset="utf-8">
<title>RK Harbor Advisors</title>
<link href="https://fonts.googleapis.com/css2?family=Lora:wght@400;700&family=Raleway:wght@400;500;700&display=swap" rel="stylesheet">
<style>
:root{
  --ink:#222;
  --muted:#555;
  --line:#333;
  --white:#fff;
  --footer:#ededed;
  --sky-top:#2f7fd0;
  --sky-mid:#8fb6e0;
  --city:#3b3f4a;
  --dusk-top:#5b5a6a;
  --dusk-mid:#c48f73;
  --dusk-low:#3a4452;
  --room-top:#3c3a38;
  --room-mid:#8a7f74;
  --room-low:#d9d4cf;
  --portrait:#2a2a2a;
}
*{margin:0;padding:0;box-sizing:border-box}
html,body{width:1200px;height:3423px;overflow:hidden;background:var(--white);color:var(--ink)}
body{font-family:"Lora",Georgia,serif;position:relative}
.site-header{position:absolute;top:0;left:0;width:1200px;height:117px}
.brand{position:absolute;display:flex;align-items:center;gap:10px;font-family:"Raleway",Arial,sans-serif;font-weight:700;color:var(--ink);letter-spacing:1px}
.brand-mark{width:26px;height:26px;border:3px solid var(--ink)}
.site-header .brand{left:200px;top:38px;font-size:20px}
.main-nav{position:absolute;right:150px;top:48px;display:flex;gap:48px;font-family:"Raleway",Arial,sans-serif;font-size:14px;letter-spacing:1px}
.photo{position:absolute;left:0;width:1200px}
.hero{top:117px;height:383px;background:linear-gradient(180deg,var(--sky-top) 0%,var(--sky-mid) 45%,var(--city) 62%,var(--sky-mid) 100%)}
.harbor{top:752px;height:418px;background:linear-gradient(180deg,var(--dusk-top) 0%,var(--dusk-mid) 40%,var(--dusk-low) 75%,var(--dusk-mid) 100%)}
.meeting{top:1655px;height:435px;background:linear-gradient(180deg,var(--room-top) 0%,var(--room-mid) 50%,var(--room-low) 100%)}
p{font-size:14px;line-height:1.65;color:var(--muted)}
.intro{position:absolute;top:575px;left:267px;width:668px}
.section-title{position:absolute;left:0;width:1200px;text-align:center;font-weight:700;font-size:20px;letter-spacing:2px}
.section-title::after{content:"";display:block;width:150px;height:1px;background:var(--line);margin:10px auto 0}
.service-title{top:1290px}
.service-col{position:absolute;top:1364px;width:500px}
.service-col.left{left:94px}
.service-col.right{left:628px}
.service-col ul{margin:10px 0 0 34px}
.service-col li{font-size:13px;line-height:1.6;color:var(--muted)}
.about-title{top:2268px;left:511px;width:auto;text-align:left}
.about-title::after{margin:10px 0 0}
.portrait{position:absolute;left:193px;top:2333px;width:214px;height:214px;border-radius:50%;background:var(--portrait)}
.portrait-caption{position:absolute;left:193px;top:2570px;width:214px;text-align:center;font-size:12px;line-height:1.5;color:var(--muted)}
.about-text{position:absolute;left:511px;top:2330px;width:592px}
.about-text p{margin-bottom:14px;font-size:13.5px}
.site-footer{position:absolute;left:0;top:3150px;width:1200px;height:273px;background:var(--footer);text-align:center}
.site-footer .brand{left:0;right:0;justify-content:center;top:70px;font-size:18px}
.contact{position:absolute;top:170px;width:1200px;font-size:13px;line-height:1.6;color:var(--muted)}
</style>
</head>
<body>
<header class="site-header">
  <div class="brand"><span class="brand-mark"></span>RK HARBOR ADVISORS</div>
  <nav class="main-nav"><span>HOME</span><span>ABOUT</span><span>SERVICES</span><span>CONTACT</span></nav>
</header>

<div class="photo hero" role="img" aria-label="City skyline and bridge at dusk reflected in the river"></div>

<p class="intro"><strong>RK Harbor Advisors</strong> is a U.S-based international consulting firm. We combined passion for success in the global business arena with hands-on experience to help foreign companies navigate the entry into U.S. markets and U.S. companies in initiating and expanding exports to foreign markets.</p>

<div class="photo harbor" role="img" aria-label="Container ship passing under a steel arch bridge at sunset"></div>

<h2 class="section-title service-title">SERVICE</h2>
<div class="service-col left">
  <p>RK Harbor Advisors helps U.S. companies with their export initiatives by:</p>
  <ul>
    <li>Identifying and developing new customers and strategic foreign markets</li>
    <li>Supporting the foreign trip steps</li>
    <li>Coordinating successful trade show visits</li>
    <li>Providing assistance with the completion of an export transaction</li>
    <li>Finding affiliated resources to support and guide companies to grow</li>
    <li>Connecting companies with other international trade experts to further support their international logistics, payment and financing arrangements, and for addressing trade regulations and legal issues</li>
  </ul>
</div>
<div class="service-col right">
  <p>RK Harbor Advisors helps foreign companies with developing the entry into U.S. markets by:</p>
  <ul>
    <li>Managing the site selection process</li>
    <li>Collecting market data</li>
    <li>Site identification and analysis</li>
    <li>Providing an appraisal of proposed incentives and financing resources</li>
    <li>The opening of local community services</li>
  </ul>
</div>

<div class="photo meeting" role="img" aria-label="Business team standing around a conference table"></div>

<h2 class="section-title about-title">ABOUT</h2>
<div class="portrait" role="img" aria-label="Portrait photo of the founder"></div>
<p class="portrait-caption">Dana Whitlock<br>CEO, RK Harbor Advisors</p>
<div class="about-text">
  <p>Dana Whitlock has over twenty years of experience in economic development, foreign direct investment and export assistance. Before founding RK Harbor Advisors she worked as Director of Global Business Development for a state economic development agency, where she led the foreign investment program and guided companies from many countries through their first steps into the U.S. market.</p>
  <p>Dana was appointed by the U.S. Secretary of Commerce to the Central District Export Council, an organization of business leaders who provide expertise in international business to small and mid-size exporters in the region. She served as Vice Chair for several years and helped plan regional programs for exporters, trade missions and international training events for local companies.</p>
  <p>Dana serves on the board of several civic groups in her state. With her strong network on both sides of the Atlantic, she has supported projects in Europe and the United States.</p>
  <p>Passionate about her community, Dana has joined several non-profit boards and organizations, including the regional arts council, the city chamber of commerce, the world trade forum and the women in international trade network, where she mentors young professionals entering the field.</p>
  <p>Dana is a graduate of Riverside State University. She obtained her undergraduate degree in finance and international business from the same university and completed the regional leadership program.</p>
</div>

<footer class="site-footer">
  <div class="brand"><span class="brand-mark"></span>RK HARBOR ADVISORS</div>
  <div class="contact">RK Harbor Advisors, LLC<br>dwhitlock@rkharbor.example<br>T: +1 (555) 014-2290</div>
</footer>
</body>
</html>
```